Ward Compass Business Card Design*

We need a business card design for our company Ward Compass. Our company is specialized in providing online consulting services regarding medical institutions, hospitals and doctors. We work with patients worldwide looking to choose between healthcare providers. We have a website you may use as a reference, where we list doctors and clinics worldwide. So we target Medical providers as well as patients worldwide.
Target Market(s)
Medical Providers and patients around the world
Industry/Entity Type
Medical
Contact Information for Business Card
Salma Derkaoui
CEO
+90 612 348 2071
info@wardcompass-example.com
www.wardcompass-example.com
14 Annakhil 3 H.R.B. Rabat, Morocco
Requirements
Must have
- Company logo/name on one full side, personal info and smaller logo and company name on the other side.
Nice to have
- Smart and elegant design

```html
<!DOCTYPE html>
<html lang="en">
<head>
<meta charset="utf-8">
<title>Ward Compass Business Card</title>
<link href="https://fonts.googleapis.com/css2?family=Montserrat:wght@500;600;700&family=Nunito+Sans:wght@400;600&display=swap" rel="stylesheet">
<style>
  :root {
    --navy: #123f66;
    --navy-text: #17406a;
    --grey-text: #5b5f63;
    --rule: #8a8d90;
    --card-white: #ffffff;
    --backdrop: #dfe2e5;
  }
  * { margin: 0; padding: 0; box-sizing: border-box; }
  html, body {
    width: 1200px;
    height: 800px;
    overflow: hidden;
    background: var(--backdrop);
  }
  .stage {
    position: relative;
    width: 1200px;
    height: 800px;
  }
  .card {
    position: absolute;
    left: 340px;
    width: 520px;
    height: 300px;
    box-shadow: 0 6px 18px rgba(0,0,0,0.18);
  }
  .card--front {
    top: 70px;
    background: var(--navy);
    display: flex;
    align-items: center;
    justify-content: center;
  }
  .card--back {
    top: 420px;
    background: var(--card-white);
  }
  .brand {
    display: flex;
    align-items: center;
    gap: 14px;
    font-family: "Montserrat", sans-serif;
    font-weight: 600;
    text-transform: uppercase;
    letter-spacing: 0.08em;
  }
  .brand__dot {
    border-radius: 50%;
    flex: none;
  }
  .card--front .brand { font-size: 30px; color: var(--card-white); }
  .card--front .brand__dot { width: 40px; height: 40px; background: var(--card-white); }
  .card--back .brand {
    position: absolute;
    top: 50px;
    left: 0;
    right: 0;
    justify-content: center;
    font-size: 24px;
    color: var(--navy-text);
  }
  .card--back .brand__dot { width: 32px; height: 32px; background: var(--navy); }
  .person {
    position: absolute;
    top: 150px;
    right: 290px;
    text-align: right;
  }
  .person__name {
    font-family: "Montserrat", sans-serif;
    font-weight: 700;
    font-size: 16px;
    letter-spacing: 0.02em;
    color: var(--navy-text);
    text-transform: uppercase;
  }
  .person__role {
    font-family: "Nunito Sans", sans-serif;
    font-size: 14px;
    color: var(--grey-text);
    margin-top: 2px;
  }
  .divider {
    position: absolute;
    left: 248px;
    top: 146px;
    width: 1px;
    height: 66px;
    background: var(--rule);
  }
  .contacts {
    position: absolute;
    left: 264px;
    top: 150px;
    list-style: none;
    font-family: "Nunito Sans", sans-serif;
    font-size: 13.5px;
    color: var(--grey-text);
  }
  .contacts li {
    display: flex;
    align-items: center;
    gap: 7px;
    line-height: 20px;
  }
  .contacts svg { width: 12px; height: 12px; flex: none; }
  .address {
    position: absolute;
    left: 60px;
    top: 236px;
    font-family: "Nunito Sans", sans-serif;
    font-size: 14px;
    color: var(--grey-text);
    letter-spacing: 0.01em;
  }
</style>
</head>
<body>
<main class="stage">
  <section class="card card--front" aria-label="Card front">
    <div class="brand">
      <span class="brand__dot"></span>
      <span class="brand__name">Ward Compass</span>
    </div>
  </section>

  <section class="card card--back" aria-label="Card back">
    <div class="brand">
      <span class="brand__dot"></span>
      <span class="brand__name">Ward Compass</span>
    </div>

    <div class="person">
      <p class="person__name">Salma Derkaoui</p>
      <p class="person__role">CEO</p>
    </div>

    <span class="divider"></span>

    <ul class="contacts">
      <li>
        <svg viewBox="0 0 24 24" aria-hidden="true"><path fill="#17406a" d="M6.6 10.8a15.1 15.1 0 0 0 6.6 6.6l2.2-2.2c.3-.3.7-.4 1-.2 1.1.4 2.3.6 3.6.6.6 0 1 .4 1 1V20c0 .6-.4 1-1 1C10.6 21 3 13.4 3 4c0-.6.4-1 1-1h3.5c.6 0 1 .4 1 1 0 1.3.2 2.5.6 3.6.1.3 0 .7-.2 1l-2.3 2.2z"/></svg>
        <span>+90 612 348 2071</span>
      </li>
      <li>
        <svg viewBox="0 0 24 24" aria-hidden="true"><rect x="2.5" y="5" width="19" height="14" fill="none" stroke="#17406a" stroke-width="2"/><path d="M3 6l9 7 9-7" fill="none" stroke="#17406a" stroke-width="2"/></svg>
        <span>info@wardcompass-example.com</span>
      </li>
      <li>
        <svg viewBox="0 0 24 24" aria-hidden="true"><g fill="none" stroke="#17406a" stroke-width="1.8"><circle cx="12" cy="12" r="9.5"/><ellipse cx="12" cy="12" rx="4" ry="9.5"/><path d="M2.5 12h19M4 7h16M4 17h16"/></g></svg>
        <span>www.wardcompass-example.com</span>
      </li>
    </ul>

    <p class="address">14 Annakhil 3 H.R.B. Rabat, Morocco</p>
  </section>
</main>
</body>
</html>
```